Helpdesk Brochure

Would like to revamp an old brochure for a conference
Can I please add our 1300 857 319 in the footer
Printing this on a double sided Brochure

```html
<!DOCTYPE html>
<html lang="en">
<head>
<meta charset="utf-8">
<title>Kestrel Desk – Double-sided Brochure</title>
<link href="https://fonts.googleapis.com/css2?family=Oswald:wght@500;600;700&family=Arimo:wght@400;700&display=swap" rel="stylesheet">
<style>
:root{
  --orange:#f26522;
  --charcoal:#3a3a3c;
  --ink:#111;
  --paper:#fff;
  --backdrop:#efefef;
  --photo-blue-a:#0e2a3a;
  --photo-blue-b:#3d7f96;
  --photo-office-a:#d9d6d2;
  --photo-office-b:#5c5c5e;
}
*{box-sizing:border-box;margin:0;padding:0}
html,body{width:1200px;height:940px;overflow:hidden;background:var(--backdrop)}
body{position:relative;font-family:"Arimo",Arial,sans-serif;color:var(--ink)}
.page{position:absolute;top:130px;width:478px;height:675px;background:var(--paper);overflow:hidden}
.page--front{left:96px}
.page--back{left:627px}
.abs{position:absolute}
.band{position:absolute;left:0;width:100%}
.band--orange{background:var(--orange)}
.band--charcoal{background:var(--charcoal)}
.banner{position:absolute;display:flex;align-items:center;justify-content:center;color:#fff;font-family:"Oswald",sans-serif;font-weight:600;letter-spacing:.3px}
.banner svg{position:absolute;inset:0;width:100%;height:100%}
.banner span{position:relative}
.service{position:absolute;width:200px}
.service-rule{position:absolute;left:0;top:-6px;width:2px;height:86px;background:var(--charcoal)}
.service-icon{position:absolute;left:-24px;top:24px;width:24px;height:24px;background:var(--orange);display:flex;align-items:center;justify-content:center}
.service-icon svg{width:15px;height:15px}
.service h3{margin-left:10px;font-family:"Oswald",sans-serif;font-weight:500;font-size:14px;color:var(--orange);line-height:1.1;text-transform:uppercase;white-space:nowrap}
.service p{margin:6px 0 0 10px;width:180px;font-size:9px;line-height:1.3}
.photo{position:absolute;left:0;width:100%}
.photo--tech{top:367px;height:207px;background:radial-gradient(circle at 60% 45%,var(--photo-blue-b),var(--photo-blue-a) 70%)}
.photo--office{top:131px;height:168px;background:linear-gradient(100deg,var(--photo-office-b) 0%,var(--photo-office-a) 45%,#f2f1ef 70%,var(--photo-office-b) 100%)}
.cta-title{font-family:"Oswald",sans-serif;font-weight:600;font-size:26px;color:var(--orange);line-height:1}
.cta-phone{display:flex;align-items:center;gap:3px;font-family:"Oswald",sans-serif;font-weight:600;font-size:24px;line-height:1;white-space:nowrap}
.cta-phone svg{width:22px;height:20px}
.contact{font-size:9px;font-weight:700;line-height:1.3;display:flex;gap:4px;align-items:flex-start}
.contact svg{width:11px;height:12px;flex:none;margin-top:1px}
.hero-kicker{font-family:"Oswald",sans-serif;font-weight:600;color:#fff;font-size:18px;line-height:1}
.hero-title{font-family:"Oswald",sans-serif;font-weight:700;color:#fff;font-size:40px;line-height:1}
.hero-sub{font-family:"Oswald",sans-serif;font-weight:500;color:#fff;font-size:12px}
.hero-note{color:#fff;font-size:8px;font-weight:700;line-height:1.25}
.brand{position:absolute;left:338px;top:36px;display:flex;align-items:center;gap:6px}
.brand-mark{width:11px;height:11px;background:var(--charcoal)}
.brand-name{font-family:"Oswald",sans-serif;font-weight:600;font-size:19px;color:var(--orange);letter-spacing:.5px;white-space:nowrap;line-height:1}
</style>
</head>
<body>

<section class="page page--front" aria-label="Brochure front: Managed IT services">
  <div class="band band--orange" style="top:0;height:11px"></div>
  <div class="band band--charcoal" style="top:15px;height:12px"></div>
  <div class="banner" style="left:64px;top:15px;width:349px;height:40px;font-size:25px">
    <svg viewBox="0 0 349 40" preserveAspectRatio="none"><polygon points="0,0 349,0 336,40 13,40" fill="var(--charcoal)"/></svg>
    <span>MANAGED I.T SERVICES</span>
  </div>

  <div class="service" style="left:42px;top:84px">
    <div class="service-rule"></div>
    <div class="service-icon"><svg viewBox="0 0 16 16"><rect x="1.5" y="2" width="13" height="9" fill="none" stroke="#fff" stroke-width="1.4"/><path d="M5 14h6M8 11v3" stroke="#fff" stroke-width="1.4"/></svg></div>
    <h3>Managed I.T Support</h3>
    <p>Optimize your business operations, providing proactive solutions and assistance to ensure smooth and efficient technology management.</p>
  </div>
  <div class="service" style="left:266px;top:84px">
    <div class="service-rule"></div>
    <div class="service-icon"><svg viewBox="0 0 16 16"><rect x="2" y="3" width="12" height="8" fill="none" stroke="#fff" stroke-width="1.3"/><path d="M1 13h14" stroke="#fff" stroke-width="1.4"/><path d="M8 4.5l2 1v2c0 1-1 1.7-2 2-1-.3-2-1-2-2v-2z" fill="#fff"/></svg></div>
    <h3>Cybersecurity Solutions</h3>
    <p>Protect your digital assets and safeguard your business, with defense mechanisms and proactive monitoring to mitigate cyber threats effectively</p>
  </div>
  <div class="service" style="left:42px;top:185px">
    <div class="service-rule"></div>
    <div class="service-icon"><svg viewBox="0 0 16 16"><path d="M4 12a3 3 0 0 1 0-6 4 4 0 0 1 8 0 3 3 0 0 1 0 6z" fill="#fff"/><path d="M8 11V7M6.5 8.5L8 7l1.5 1.5" stroke="var(--orange)" stroke-width="1.2" fill="none"/></svg></div>
    <h3>Cloud Servers &amp; Backups</h3>
    <p>Secure your data, ensuring reliable storage, seamless accessibility, and robust disaster recovery capabilities for your business</p>
  </div>
  <div class="service" style="left:266px;top:185px">
    <div class="service-rule"></div>
    <div class="service-icon"><svg viewBox="0 0 16 16"><rect x="2" y="2" width="5.5" height="5.5" fill="#fff"/><rect x="8.5" y="2" width="5.5" height="5.5" fill="#fff"/><rect x="2" y="8.5" width="5.5" height="5.5" fill="#fff"/><rect x="8.5" y="8.5" width="5.5" height="5.5" fill="#fff"/></svg></div>
    <h3>Cloud Office Email Packs</h3>
    <p>Elevate your email communication, providing advanced features, security enhancements, and seamless integration.</p>
  </div>
  <div class="service" style="left:146px;top:277px">
    <div class="service-rule"></div>
    <div class="service-icon"><svg viewBox="0 0 16 16" fill="none" stroke="#fff" stroke-width="1.2"><circle cx="8" cy="8" r="6"/><ellipse cx="8" cy="8" rx="2.6" ry="6"/><path d="M2 8h12M3 5h10M3 11h10"/></svg></div>
    <h3>Domains &amp; Websites</h3>
    <p>Establish your online presence with ease, offering personalised domain registration, expert website design, and reliable hosting solutions for your business</p>
  </div>

  <div class="photo photo--tech" role="img" aria-label="Photo of a hand touching a glowing digital interface of support icons"></div>

  <div class="abs" style="left:71px;top:588px">
    <div class="cta-title">GET IN TOUCH</div>
    <div class="cta-phone"><svg viewBox="0 0 22 20"><rect x="1" y="3" width="10" height="16" fill="var(--charcoal)"/><rect x="3" y="5" width="6" height="3" fill="#fff"/><path d="M14 6q3 4 0 8M17 4q5 6 0 12" stroke="var(--charcoal)" stroke-width="1.6" fill="none"/></svg>1300 857 319</div>
  </div>
  <div class="abs" style="left:252px;top:592px">
    <div class="contact"><svg viewBox="0 0 12 14"><path d="M6 13S1 8 1 5a5 5 0 0 1 10 0c0 3-5 8-5 8z" fill="var(--orange)"/><circle cx="6" cy="5" r="1.8" fill="#fff"/></svg><span>12/48 Larkin Street,<br>Brookvale VIC 3090</span></div>
    <div class="contact" style="margin-top:8px"><svg viewBox="0 0 12 12"><rect x="1" y="2.5" width="10" height="7" fill="none" stroke="var(--orange)" stroke-width="1.3"/><path d="M1 2.5l5 4 5-4" fill="none" stroke="var(--orange)" stroke-width="1.3"/></svg><span>sales@kestreldesk.com.au</span></div>
  </div>

  <div class="band band--orange" style="top:649px;height:15px"></div>
  <div class="band band--charcoal" style="top:667px;height:8px"></div>
</section>

<section class="page page--back" aria-label="Brochure back: Cloud phone systems and internet">
  <svg class="abs" style="left:0;top:0" width="478" height="131" viewBox="0 0 478 131">
    <rect width="478" height="131" fill="var(--orange)"/>
    <polygon points="231,0 478,0 478,105 327,105" fill="#fff"/>
    <polygon points="256,28 268,28 330,105 318,105" fill="var(--ink)"/>
  </svg>
  <div class="abs" style="left:27px;top:18px">
    <div class="hero-kicker">MELBOURNE'S LEADING</div>
    <div class="hero-title">IT SUPPORT</div>
    <div class="hero-sub" style="margin-top:7px">TAKING CARE OF YOUR IT HEADACHES</div>
    <div class="hero-note" style="margin-top:2px">We partner with all types of businesses to solve their IT problems<br>with continuous ongoing support and solutions that work</div>
  </div>
  <div class="brand">
    <span class="brand-mark"></span>
    <span class="brand-name">KESTREL DESK</span>
  </div>

  <div class="photo photo--office" role="img" aria-label="Photo of an office desk with a laptop, coffee mug, clock and pencil cup"></div>

  <div class="band band--orange" style="top:301px;height:4px"></div>
  <div class="band band--charcoal" style="top:307px;height:7px"></div>
  <div class="banner" style="left:64px;top:307px;width:351px;height:33px;font-size:21px">
    <svg viewBox="0 0 351 33" preserveAspectRatio="none"><polygon points="0,0 351,0 340,33 11,33" fill="var(--charcoal)"/></svg>
    <span>CLOUD PHONE SYSTEMS &amp; INTERNET</span>
  </div>

  <div class="service" style="left:44px;top:372px">
    <div class="service-rule"></div>
    <div class="service-icon"><svg viewBox="0 0 16 16"><path d="M4 2l2.5 3-1.5 1.5c.8 1.8 2.2 3.2 4 4L10.5 9l3 2.5-1.5 2.5C7 14 2 9 1.8 4z" fill="#fff"/></svg></div>
    <h3>VOIP &amp; Phone Systems</h3>
    <p>We provide expert services in installation and management for office phone lines, VoIP and communications hardware and systems</p>
  </div>
  <div class="service" style="left:266px;top:372px">
    <div class="service-rule"></div>
    <div class="service-icon"><svg viewBox="0 0 16 16"><path d="M2 3h12v8H7l-3 3v-3H2z" fill="#fff"/><circle cx="5.5" cy="7" r="1" fill="var(--orange)"/><circle cx="8" cy="7" r="1" fill="var(--orange)"/><circle cx="10.5" cy="7" r="1" fill="var(--orange)"/></svg></div>
    <h3>SMS Gateway</h3>
    <p>Unlock seamless communication with our cutting-edge SMS Gateway services, ensuring instant and reliable message delivery for your business needs.</p>
  </div>
  <div class="service" style="left:44px;top:474px">
    <div class="service-rule"></div>
    <div class="service-icon"><svg viewBox="0 0 16 16" fill="#fff"><circle cx="8" cy="5" r="2.2"/><circle cx="3.5" cy="6" r="1.6"/><circle cx="12.5" cy="6" r="1.6"/><path d="M4 12a4 4 0 0 1 8 0zM0.5 11.5a3 3 0 0 1 4.5-2.5 5 5 0 0 0-1.3 2.5zM15.5 11.5a3 3 0 0 0-4.5-2.5 5 5 0 0 1 1.3 2.5z"/></svg></div>
    <h3>Unified Team Calling</h3>
    <p>Experience the next level of collaboration with our Unified Team calling services, empowering your team with seamless communication and features.</p>
  </div>
  <div class="service" style="left:266px;top:474px">
    <div class="service-rule"></div>
    <div class="service-icon"><svg viewBox="0 0 16 16" fill="none" stroke="#fff" stroke-width="1.2"><circle cx="8" cy="8" r="6"/><ellipse cx="8" cy="8" rx="2.6" ry="6"/><path d="M2 8h12M3 5h10M3 11h10"/></svg></div>
    <h3>Broadband, Fibre &amp; 4G Internet</h3>
    <p>Stay connected, delivering reliable and high-speed connectivity tailored to your business requirements</p>
  </div>

  <div class="abs" style="left:23px;top:578px">
    <div class="contact"><svg viewBox="0 0 12 14"><path d="M6 13S1 8 1 5a5 5 0 0 1 10 0c0 3-5 8-5 8z" fill="var(--orange)"/><circle cx="6" cy="5" r="1.8" fill="#fff"/></svg><span>12/48 Larkin Street,<br>Brookvale VIC 3090</span></div>
    <div class="contact" style="margin-top:8px"><svg viewBox="0 0 12 12"><rect x="1" y="2.5" width="10" height="7" fill="none" stroke="var(--orange)" stroke-width="1.3"/><path d="M1 2.5l5 4 5-4" fill="none" stroke="var(--orange)" stroke-width="1.3"/></svg><span>sales@kestreldesk.com.au</span></div>
  </div>
  <svg class="abs" style="left:191px;top:575px" width="287" height="68" viewBox="0 0 287 68"><polygon points="54,0 287,0 287,68 0,68" fill="var(--charcoal)"/></svg>
  <div class="abs" style="left:238px;top:582px;text-align:right;width:220px">
    <div class="cta-title" style="color:#fff;font-size:22px">GET IN TOUCH</div>
    <div class="cta-phone" style="color:#fff;font-size:29px;justify-content:flex-end"><svg viewBox="0 0 22 20"><rect x="1" y="3" width="10" height="16" fill="#fff"/><rect x="3" y="5" width="6" height="3" fill="var(--charcoal)"/><path d="M14 6q3 4 0 8M17 4q5 6 0 12" stroke="#fff" stroke-width="1.6" fill="none"/></svg>1300 857 319</div>
  </div>

  <div class="band band--orange" style="top:646px;height:18px"></div>
  <div class="band band--charcoal" style="top:667px;height:8px"></div>
</section>

</body>
</html>
```